Business Card for supplement company

Company Name: Pinevale Nutrition
We require quite a simple yet stand out business card for our supplement company.
We are selling high end bodybuilding supplements direct to the public through online sales and Facebook marketing.
There will be slightly varying versions of the card and the winning design will be required to make these slight adjustments.
We will also require the file to be provided in and editable version as we will have a discount code on there that will be changed for different people.
Employee Cards:
Logo on the front of the card (see attached EPS file)
Please also add slogan in text "When Failure is Not and Option" as close as possible to what is seen in this link www.pinevalenutrition.com.au
Suggestions: Card in black, possibly use a similar background to website theme (honeycomb, carbon look)
Information to be included on the back (please place and order accordingly)
:Clive Marrowby (Director)
Email: clive@pinevalenutrition.com.au
Phone: 02 5918 2273
Website: www.pinevalenutrition.com.au
Athlete Cards:
Front:
Same as above
Back:
Discount Code: xxx123 (to be editable)
Facebook: www.facebook.com/PinevaleNutrition
Design ideas: please look at our website and facebook signup page for design ideas.

```html
<!DOCTYPE html>
<html lang="en">
<head>
<meta charset="utf-8">
<title>Pinevale Nutrition – Business Cards</title>
<link href="https://fonts.googleapis.com/css2?family=Jost:wght@400;500&family=Open+Sans:wght@400;700&display=swap" rel="stylesheet">
<style>
  :root {
    --bg-light: #d4d4d4;
    --bg-dark: #4a4a4a;
    --card: #0b0b0b;
    --card-edge: #1c1c1c;
    --green: #4cc43f;
    --green-deep: #1f7a22;
    --yellow: #e4d90a;
    --white: #f2f2f2;
    --grey-text: #cfcfcf;
  }
  * { box-sizing: border-box; margin: 0; padding: 0; }
  html, body { width: 1200px; height: 900px; overflow: hidden; }
  body {
    background: radial-gradient(ellipse at 30% 20%, var(--bg-light) 0%, #a9a9a9 45%, var(--bg-dark) 100%);
    position: relative;
    font-family: "Open Sans", Arial, sans-serif;
  }
  .card {
    position: absolute;
    width: 470px;
    height: 280px;
    border-radius: 16px;
    background: var(--card);
    border: 1px solid var(--card-edge);
    box-shadow: 0 14px 30px rgba(0,0,0,.35);
    overflow: hidden;
  }
  .brand-name {
    font-family: "Jost", "Futura", sans-serif;
    font-weight: 500;
    color: var(--green);
    text-align: center;
    letter-spacing: 2px;
    line-height: 1.1;
  }

  /* Front card */
  .card--front { left: 80px; top: 60px; }
  .card--front .brand-name { font-size: 40px; margin-top: 72px; }
  .slogan {
    font-family: "Jost", "Futura", sans-serif;
    color: var(--yellow);
    font-size: 21px;
    text-align: center;
    margin-top: 34px;
  }

  /* Employee back */
  .card--employee { left: 650px; top: 320px; }
  .card__texture {
    position: absolute; inset: 0;
    background: radial-gradient(ellipse at 70% 20%, #2a2a2a 0%, #151515 50%, #080808 100%);
  }
  .card--employee .brand-name {
    position: absolute; left: 40px; top: 50px;
    font-size: 30px; text-align: left;
  }
  .name-band {
    position: absolute; right: 0; top: 148px;
    width: 230px; height: 24px;
    background: linear-gradient(90deg, rgba(76,196,63,0) 0%, var(--green-deep) 35%, var(--green) 100%);
  }
  .person-name {
    position: absolute; right: 18px; top: 149px;
    font-weight: 700; font-size: 15px; color: var(--yellow); letter-spacing: .5px;
  }
  .person-role {
    position: absolute; right: 18px; top: 178px;
    font-size: 10px; color: var(--white); letter-spacing: .5px;
  }
  .contact-list {
    position: absolute; left: 245px; top: 200px;
    list-style: none;
  }
  .contact-list li {
    display: flex; align-items: center; gap: 8px;
    font-size: 11.5px; color: var(--white); margin-bottom: 4px;
  }
  .contact-list svg { width: 13px; height: 13px; flex: none; }

  /* Athlete back */
  .card--athlete { left: 80px; top: 560px; }
  .card--athlete .brand-name { font-size: 34px; margin-top: 48px; }
  .discount-band {
    position: absolute; left: 0; top: 150px; width: 100%; height: 36px;
    background: linear-gradient(180deg, #143f14 0%, var(--green-deep) 50%, #0d2a0d 100%);
    box-shadow: 0 6px 14px rgba(76,196,63,.25);
    text-align: center; line-height: 36px;
    font-family: "Jost", "Futura", sans-serif;
    font-size: 16px; color: var(--yellow);
  }
  .athlete-links {
    position: absolute; left: 0; top: 200px; width: 100%;
    text-align: center; font-size: 11.5px; color: var(--white); line-height: 1.5;
  }
  .athlete-links b { color: var(--green); font-weight: 700; }
</style>
</head>
<body>

  <section class="card card--front">
    <p class="brand-name">Pinevale Nutrition</p>
    <p class="slogan">When Failure is Not and Option!</p>
  </section>

  <section class="card card--employee">
    <div class="card__texture" role="img" aria-label="Dark grunge texture background"></div>
    <p class="brand-name">Pinevale Nutrition</p>
    <div class="name-band"></div>
    <p class="person-name">CLIVE MARROWBY</p>
    <p class="person-role">DIRECTOR</p>
    <ul class="contact-list">
      <li>
        <svg viewBox="0 0 14 14"><rect width="14" height="14" rx="2" fill="#4cc43f"/><path d="M4 3.5l2 2-1 1.2c.6 1.2 1.5 2.1 2.6 2.7l1.2-1 2 2-1.3 1.3C6.5 11.5 2.8 7.7 2.7 4.8z" fill="#0b0b0b"/></svg>
        02 5918 2273
      </li>
      <li>
        <svg viewBox="0 0 14 14"><rect width="14" height="14" rx="2" fill="#4cc43f"/><rect x="3" y="4" width="8" height="6" fill="none" stroke="#0b0b0b" stroke-width="1.2"/><path d="M3 4l4 3.5L11 4" fill="none" stroke="#0b0b0b" stroke-width="1.2"/></svg>
        clive@pinevalenutrition.com.au
      </li>
      <li>
        <svg viewBox="0 0 14 14"><rect width="14" height="14" rx="2" fill="#4cc43f"/><circle cx="7" cy="7" r="4" fill="none" stroke="#0b0b0b" stroke-width="1.1"/><path d="M3 7h8M7 3c-2 2.4-2 5.6 0 8M7 3c2 2.4 2 5.6 0 8" fill="none" stroke="#0b0b0b" stroke-width=".9"/></svg>
        www.pinevalenutrition.com.au
      </li>
    </ul>
  </section>

  <section class="card card--athlete">
    <p class="brand-name">Pinevale Nutrition</p>
    <div class="discount-band">Discount Code: xxxx-xxx-xxx</div>
    <p class="athlete-links">
      <b>Website:</b> www.pinevalenutrition.com.au<br>
      <b>Facebook:</b> www.facebook.com/PinevaleNutrition
    </p>
  </section>

</body>
</html>
```